Redesign of PTO Calendar website

Looking to drastically improve our PTO (paid time off) Calendar look and feel. Need a modern and well thought out design that is fun.
Current Screenshots
https://files.brindlemoor.net/sheet/p/7vTq2LmW9xZpK4nRb8JsYcHa3eDfG5uNwQ1tVhXo/view?mode=public
It's written in PHP and Laravel, if that matters. I am not necessarily attached to any of the current design, so please go wild. Current functionality needs to remain the same, but some can be added if you feel it would be of value. Layout can certainly change.
NOTE - this calendar can be used by any company, not just our own. So we'd like it to have a look and feel that is easy to navigate.
Site logo is attached.
Pages needed:
* Login Page
* Registration Page
* Calendar page
* Add PTO method
* Admin page (will use template for all admin areas)
* User profile page
Thanks!

```html
<!DOCTYPE html>
<html lang="en">
<head>
<meta charset="utf-8">
<title>Restday – PTO Calendar Screens</title>
<link rel="stylesheet" href="https://fonts.googleapis.com/css2?family=Poppins:wght@400;500;600;700&display=swap">
<style>
:root{
  --canvas:#3f4b5b;
  --blue:#0b74c1;
  --ink:#2f3a4a;
  --text:#4a5462;
  --muted:#8d96a3;
  --line:#dde1e6;
  --surface:#ffffff;
  --screen-bg:#f7f8fa;
  --app-bg:#eef0f3;
  --header-dark:#3e4a5b;
  --avatar-green:#7dd35a;
  --event-green:#7ea46a;
  --event-orange:#f5a432;
  --highlight:#fdf1dc;
  --badge-bg:#e3f3e1;
  --badge-text:#5da25a;
  --danger:#e35b5b;
}
*{box-sizing:border-box;margin:0;padding:0}
h1,h2{font-weight:400}
html,body{width:759px;height:1200px;overflow:hidden}
body{background:var(--canvas);font-family:"Poppins",sans-serif;color:var(--text);position:relative}

/* Hero wordmark */
.hero-brand{position:absolute;left:0;top:100px;width:759px;height:104px;display:flex;align-items:center;justify-content:center;gap:14px}
.hero-brand__name{font:600 72px/1 "Poppins",sans-serif;color:#fff;letter-spacing:-1px}
.hero-brand__dot{width:100px;height:100px;border-radius:50%;background:var(--blue)}

/* Screen frames */
.screen{position:absolute;width:279px;height:226px;background:var(--screen-bg);overflow:hidden}
.screen--login{left:84px;top:281px}
.screen--signup{left:391px;top:341px}
.screen--calendar{left:84px;top:530px;background:var(--app-bg)}
.screen--add-pto{left:395px;top:593px;background:var(--app-bg)}
.screen--teams{left:84px;top:780px;background:var(--surface)}
.screen--profile{left:391px;top:844px;background:var(--app-bg)}

.brand{position:absolute;display:flex;align-items:center;gap:2px;font:600 7px/1 "Poppins",sans-serif;color:var(--ink)}
.brand__dot{width:7px;height:7px;border-radius:50%;background:var(--blue)}
.screen--login .brand,.screen--signup .brand{left:20px;top:9px}

.auth-switch{position:absolute;right:20px;top:11px;font-size:3.6px;color:var(--ink)}
.auth-switch a{color:var(--blue);text-decoration:none;font-weight:500}

.auth-card{position:absolute;left:97px;top:32px;width:85px;background:var(--surface);border-radius:2px;box-shadow:0 1px 3px rgba(0,0,0,.06)}
.auth-card > *{position:absolute}
.auth-card__eyebrow{left:0;width:100%;text-align:center;font-size:3.8px;font-weight:500;color:var(--blue)}
.auth-card__title{left:0;width:100%;text-align:center;font-size:6.6px;font-weight:400;color:var(--ink)}
.auth-card__rule{left:38.5px;width:8px;height:.6px;background:var(--blue)}
.auth-card__lead{left:0;width:100%;text-align:center;font-size:4.2px;font-weight:500;color:var(--ink)}
.social-row{left:15px;display:flex;gap:2px}
.social-btn{width:17px;height:16.5px;border:.5px solid var(--line);border-radius:1.5px;background:#fff;display:flex;align-items:center;justify-content:center;font-size:3.4px;font-weight:500;color:var(--ink);box-shadow:0 .5px 1px rgba(0,0,0,.05)}
.or-divider{left:7px;width:71px;display:flex;align-items:center;gap:3px;font-size:3px;color:var(--muted)}
.or-divider::before,.or-divider::after{content:"";flex:1;height:.4px;background:var(--line)}
.field{left:7px;width:71px;height:12.5px;border:.5px solid #cfd4da;border-radius:1.5px;background:#fff;font-size:4px;color:var(--ink);padding-left:5px;display:flex;align-items:center}
.check-row{left:7px;width:72px;display:flex;justify-content:space-between;font-size:3.4px;color:var(--ink)}
.check{display:inline-block;width:4.5px;height:4.5px;border-radius:.8px;background:var(--blue);vertical-align:middle;margin-right:2px;position:relative}
.check::after{content:"";position:absolute;left:1.4px;top:.5px;width:1.2px;height:2.3px;border:solid #fff;border-width:0 .5px .5px 0;transform:rotate(45deg)}
.link{color:var(--blue);text-align:right;line-height:1.3}
.primary-btn{left:7px;width:71px;height:13px;border-radius:1.5px;background:var(--blue);color:#fff;font-size:4.2px;font-weight:600;display:flex;align-items:center;justify-content:center}
.ghost-btn{position:absolute;left:104px;top:186px;width:71px;height:13px;border:.5px solid #c5cbd2;border-radius:1.5px;background:#fff;color:var(--blue);font-size:4px;display:flex;align-items:center;justify-content:center}
.terms-note{left:7px;width:72px;font-size:2.4px;line-height:1.35;color:var(--text);padding-left:7px}

/* App chrome */
.app-bar{position:absolute;left:0;top:0;width:100%;height:17.5px;background:#fff;border-bottom:.5px solid #e6e9ed}
.app-bar .brand{left:6px;top:5px}
.app-nav{position:absolute;left:46px;top:4.5px;display:flex;gap:4.5px;align-items:center;font-size:3.6px;color:var(--ink)}
.app-nav__item{display:flex;align-items:center;gap:3px}
.app-nav__icon{width:7.5px;height:7.5px;border-radius:1px;display:flex;align-items:center;justify-content:center;background:#fff;box-shadow:0 .4px 1.2px rgba(0,0,0,.12)}
.app-nav__icon svg{width:4px;height:4px}
.app-nav__item--active .app-nav__icon{background:var(--blue)}
.user-chip{position:absolute;right:6px;top:3.5px;display:flex;align-items:center;gap:3px;font-size:4px;color:var(--ink)}
.avatar{border-radius:50%;background:var(--avatar-green);color:#fff;font-weight:600;display:flex;align-items:center;justify-content:center}
.user-chip .avatar{width:10px;height:10px;font-size:4px}
.user-chip__caret{width:2px;height:2px;border:solid var(--muted);border-width:0 .4px .4px 0;transform:rotate(45deg);margin-left:1px;margin-top:-1px}

.content-card{position:absolute;left:6px;top:20px;width:267px;height:230px;background:#fff;border-radius:2px;box-shadow:0 1px 3px rgba(0,0,0,.05)}

/* Calendar page */
.sidebar-title{position:absolute;left:16px;top:35px;font-size:3.8px;font-weight:500;color:var(--ink)}
.search-box{position:absolute;height:9.5px;border:.5px solid #d3d8de;border-radius:1.5px;background:#fff;font-size:3.2px;color:var(--muted);display:flex;align-items:center;justify-content:space-between;padding:0 3px}
.search-box svg{width:4px;height:4px}
.screen--calendar .search-box,.screen--add-pto .search-box{left:16px;top:41.5px;width:54px}
.employee{position:absolute;left:17px;top:55px;display:flex;gap:3px;align-items:center}
.employee .avatar{width:10px;height:10px;font-size:4px}
.employee__name{font-size:4px;color:var(--ink);line-height:1}
.employee__type{font-size:3.2px;color:var(--muted);line-height:1}
.cal-controls{position:absolute;left:79px;top:41.5px;display:flex;gap:2.5px}
.ctrl-btn{height:9.5px;border:.5px solid #cfd4da;border-radius:1.5px;background:#fff;font-size:3.4px;color:var(--ink);display:flex;align-items:center;justify-content:center}
.ctrl-btn--icon{width:7.5px}
.ctrl-btn--today{width:16.5px;margin-left:1px}
.cal-title{position:absolute;left:120px;width:98px;top:43px;text-align:center;font-size:5.6px;font-weight:400;color:var(--ink)}
.view-switch{position:absolute;left:220px;top:41.5px;display:flex;height:9.5px;border:.5px solid #cfd4da;border-radius:1.5px;overflow:hidden;font-size:3.4px;color:var(--ink);background:#fff}
.view-switch span{display:flex;align-items:center;padding:0 3px}
.view-switch .is-active{background:var(--blue);color:#fff;padding:0 4.5px}
.cal{position:absolute;left:79px;top:56px;width:186px}
.cal__head{display:grid;grid-template-columns:repeat(7,1fr);height:11px;background:var(--header-dark);border-radius:1.5px 1.5px 0 0;color:#fff;font-size:3.6px;font-weight:600}
.cal__head span{display:flex;align-items:center;justify-content:center}
.cal__body{display:grid;grid-template-columns:repeat(7,1fr);grid-auto-rows:20.3px;border-left:.5px solid var(--line)}
.cal__body span{border-right:.5px solid var(--line);border-bottom:.5px solid var(--line);font-size:3px;color:var(--muted);text-align:right;padding:3px 3px 0 0;background:#fff}
.cal__body .is-highlight{background:var(--highlight)}
.cal-event{position:absolute;height:5px;font-size:2.8px;font-weight:500;color:#fff;display:flex;align-items:center;padding-left:4px;white-space:nowrap}
.cal-event--green{left:79.7px;top:40.5px;width:53px;background:var(--event-green)}
.cal-event--blue{left:79.7px;top:46.5px;width:68px;background:var(--blue)}
.cal-event--orange{left:0;top:86px;width:80px;height:6.5px;background:var(--event-orange);font-size:3.2px}

/* Add PTO dialog */
.scrim{position:absolute;inset:0;background:rgba(80,90,105,.38)}
.dialog{position:absolute;left:97px;top:40px;width:85px;height:145px;background:#fff;border-radius:2px;box-shadow:0 2px 6px rgba(0,0,0,.15)}
.dialog > *{position:absolute}
.dialog__title{left:0;width:100%;top:12px;text-align:center;font-size:6.4px;font-weight:400;color:var(--ink)}
.dialog__rule{left:38.5px;top:22px;width:8px;height:.6px;background:var(--blue)}
.dialog__label{left:7px;font-size:3.6px;color:var(--ink)}
.dialog .field{justify-content:space-between;padding-right:4px}
.dialog .field svg{width:4px;height:4px}
.dialog__btn{top:119px;width:35px;height:13px;border-radius:1.5px;font-size:4px;font-weight:600;display:flex;align-items:center;justify-content:center}
.dialog__btn--close{left:7px;border:.6px solid var(--ink);color:var(--ink);background:#fff}
.dialog__btn--save{left:43px;background:var(--blue);color:#fff}

/* Teams admin */
.screen--teams .search-box{left:6px;top:23px;width:50px}
.entries{position:absolute;right:6px;top:24px;display:flex;align-items:center;gap:3px;font-size:3.4px;color:var(--muted)}
.entries__select{border:.5px solid #d3d8de;border-radius:1px;padding:1px 2px;color:var(--ink);font-weight:600}
.data-table{position:absolute;left:6px;top:36px;width:268px;border-collapse:collapse;table-layout:fixed;font-size:3.6px;color:var(--ink);box-shadow:0 1px 3px rgba(0,0,0,.06)}
.data-table th{height:13px;background:var(--header-dark);color:#fff;font-weight:600;text-align:left;padding-left:7px;font-size:3.6px}
.data-table th:first-child{border-radius:2px 0 0 0}
.data-table th:last-child{border-radius:0 2px 0 0}
.data-table td{height:17.7px;padding-left:7px;vertical-align:middle}
.data-table tr:nth-child(even) td{background:#f5f6f8}
.data-table .desc{font-size:3.2px;line-height:1.3;padding-right:4px}
.data-table .count{padding-left:20px}
.badge{display:inline-block;background:var(--badge-bg);color:var(--badge-text);font-size:2.4px;font-weight:600;padding:1px 3px;border-radius:3px}
.row-actions{display:flex;gap:1.5px}
.row-actions svg{width:4px;height:4px}
.table-info{position:absolute;left:6px;top:206px;font-size:3.6px;color:var(--ink)}
.pager{position:absolute;right:6px;top:205px;display:flex;align-items:center;gap:2.5px;font-size:2.6px;color:var(--ink)}
.pager__edge{height:7px;padding:0 5px;border-radius:1px;display:flex;align-items:center;background:#eceef1;color:var(--muted)}
.pager__edge--next{background:var(--blue);color:#fff;padding:0 6px}
.pager__page{width:7px;height:7px;display:flex;align-items:center;justify-content:center}
.pager__page--active{background:var(--header-dark);color:#fff;border-radius:1px}

/* Profile */
.profile-card{position:absolute;left:6px;top:21px;width:267px;height:220px;background:#fff;border-radius:2px}
.profile-card .avatar{position:absolute;left:38px;top:20px;width:44px;height:44px;font-size:16px}
.profile-name{position:absolute;left:0;width:120px;top:91px;text-align:center;font-size:6px;color:var(--ink)}
.profile-email{position:absolute;left:0;width:120px;top:99px;text-align:center;font-size:4.8px;color:var(--blue)}
.account{position:absolute;left:115px;top:0;width:121px}
.account > *{position:absolute;left:0}
.account__title{top:22px;font-size:8px;font-weight:500;color:var(--ink)}
.account__label{font-size:3.8px;color:var(--ink)}
.account .field{width:121px;left:0}
.account .field--select{justify-content:space-between;padding-right:5px}
.flag{display:inline-block;width:6px;height:4px;background:var(--blue);border-radius:.5px;margin-right:3px;vertical-align:middle}
.caret{width:2.4px;height:2.4px;border:solid var(--ink);border-width:0 .5px .5px 0;transform:rotate(45deg);margin-top:-1.5px}
.account__save{top:172px;width:42px;height:13px;background:var(--blue);color:#fff;font-size:5px;font-weight:600;display:flex;align-items:center;justify-content:center;border-radius:1px}
</style>
</head>
<body>

<div class="hero-brand">
  <span class="hero-brand__name">Restday</span>
  <span class="hero-brand__dot"></span>
</div>

<!-- Sign in -->
<section class="screen screen--login">
  <div class="brand"><span>Restday</span><span class="brand__dot"></span></div>
  <p class="auth-switch">You do not have an account? <a href="#">Sign up</a></p>
  <div class="auth-card" style="height:148px">
    <p class="auth-card__eyebrow" style="top:11px">SIGN IN</p>
    <h1 class="auth-card__title" style="top:15px">Welcome back</h1>
    <span class="auth-card__rule" style="top:26px"></span>
    <p class="auth-card__lead" style="top:33px">Continue with...</p>
    <div class="social-row" style="top:43px">
      <span class="social-btn">Zorvi</span><span class="social-btn">Mulqa</span><span class="social-btn">Teqin</span>
    </div>
    <div class="or-divider" style="top:65px">OR</div>
    <div class="field" style="top:78px">Email</div>
    <div class="field" style="top:93px">Password</div>
    <div class="check-row" style="top:108px">
      <span><i class="check"></i>Remember me</span>
      <span class="link">Forgot your<br>password?</span>
    </div>
    <div class="primary-btn" style="top:124px">SIGN IN</div>
  </div>
  <div class="ghost-btn">Don't have an account?</div>
</section>

<!-- Sign up -->
<section class="screen screen--signup">
  <div class="brand"><span>Restday</span><span class="brand__dot"></span></div>
  <p class="auth-switch">Already have an account? <a href="#">Login</a></p>
  <div class="auth-card" style="height:172px">
    <p class="auth-card__eyebrow" style="top:12px">SIGN UP</p>
    <h1 class="auth-card__title" style="top:16px">PTO Calendar</h1>
    <span class="auth-card__rule" style="top:27px"></span>
    <p class="auth-card__lead" style="top:34px">Register with...</p>
    <div class="social-row" style="top:44px">
      <span class="social-btn">Zorvi</span><span class="social-btn">Mulqa</span><span class="social-btn">Teqin</span>
    </div>
    <div class="or-divider" style="top:67px">OR</div>
    <div class="field" style="top:79px">Name</div>
    <div class="field" style="top:94px">Last name</div>
    <div class="field" style="top:109px">Work email</div>
    <div class="check-row" style="top:127px;justify-content:flex-start">
      <span><i class="check"></i>I accept the <b style="color:var(--ink);font-weight:600">Privacy Policy</b></span>
    </div>
    <p class="terms-note" style="top:133px">By creating your account you will be accepting the Terms and Conditions of Tallyworks.</p>
    <div class="primary-btn" style="top:146px">SIGN UP</div>
  </div>
</section>

<!-- Calendar -->
<section class="screen screen--calendar">
  <header class="app-bar">
    <div class="brand"><span>Restday</span><span class="brand__dot"></span></div>
    <nav class="app-nav">
      <span class="app-nav__item"><span class="app-nav__icon"><svg viewBox="0 0 10 10"><path d="M5 1 9 9H1Z" fill="none" stroke="#3e4a5b" stroke-width="1.2"/></svg></span>Teams</span>
      <span class="app-nav__item"><span class="app-nav__icon"><svg viewBox="0 0 10 10"><circle cx="5" cy="3.2" r="2" fill="#3e4a5b"/><path d="M1.5 9.5a3.5 3.5 0 0 1 7 0Z" fill="#3e4a5b"/></svg></span>Members</span>
      <span class="app-nav__item"><span class="app-nav__icon"><svg viewBox="0 0 10 10"><rect x="1" y="1.5" width="8" height="5.5" fill="none" stroke="#3e4a5b" stroke-width="1.2"/><path d="M3 9h4" stroke="#3e4a5b" stroke-width="1.2"/></svg></span>PTO Types</span>
      <span class="app-nav__item app-nav__item--active"><span class="app-nav__icon"><svg viewBox="0 0 10 10"><rect x="1" y="1.5" width="8" height="7.5" fill="#fff"/><rect x="1" y="1.5" width="8" height="2" fill="#cfe3f3"/></svg></span>Add PTO</span>
    </nav>
    <div class="user-chip"><span class="avatar">DM</span>Daniel Marsh<span class="user-chip__caret"></span></div>
  </header>
  <div class="content-card"></div>
  <p class="sidebar-title">EMPLOYE</p>
  <div class="search-box">Search Employees<svg viewBox="0 0 10 10"><circle cx="4.2" cy="4.2" r="3" fill="none" stroke="#0b74c1" stroke-width="1.3"/><path d="m6.5 6.5 2.5 2.5" stroke="#0b74c1" stroke-width="1.3"/></svg></div>
  <div class="employee"><span class="avatar">DM</span><div><p class="employee__name">Daniel Marsh</p><p class="employee__type">Vacation</p></div></div>
  <div class="cal-controls"><span class="ctrl-btn ctrl-btn--icon">‹</span><span class="ctrl-btn ctrl-btn--icon">›</span><span class="ctrl-btn ctrl-btn--today">Today</span></div>
  <h2 class="cal-title">August 2020</h2>
  <div class="view-switch"><span class="is-active">Month</span><span>Week</span><span>Day</span></div>
  <div class="cal">
    <div class="cal__head"><span>Sun</span><span>Mon</span><span>Tue</span><span>Wed</span><span>Thu</span><span>Fri</span><span>Sat</span></div>
    <div class="cal__body">
      <span>26</span><span>27</span><span>28</span><span>29</span><span>30</span><span>31</span><span>1</span>
      <span>2</span><span>3</span><span>4</span><span>5</span><span>6</span><span>7</span><span>8</span>
      <span>9</span><span>10</span><span>11</span><span>12</span><span>13</span><span>14</span><span>15</span>
      <span class="is-highlight">16</span><span>17</span><span>18</span><span>19</span><span>20</span><span>21</span><span>22</span>
      <span>23</span><span>24</span><span>25</span><span>26</span><span>27</span><span>28</span><span>29</span>
      <span>30</span><span>31</span><span>1</span><span>2</span><span>3</span><span>4</span><span>5</span>
      <span>6</span><span>7</span><span>8</span><span>9</span><span>10</span><span>11</span><span>12</span>
      <span>13</span><span>14</span><span>15</span><span>16</span><span>17</span><span>18</span><span>19</span>
    </div>
    <span class="cal-event cal-event--green">12a Ryan Marsh-Vacation</span>
    <span class="cal-event cal-event--blue">4a Clara Owens-Vacation</span>
    <span class="cal-event cal-event--orange">Daniel Marsh-Vacation</span>
  </div>
</section>

<!-- Add PTO dialog over calendar -->
<section class="screen screen--add-pto">
  <header class="app-bar">
    <div class="brand"><span>Restday</span><span class="brand__dot"></span></div>
    <nav class="app-nav">
      <span class="app-nav__item"><span class="app-nav__icon"><svg viewBox="0 0 10 10"><path d="M5 1 9 9H1Z" fill="none" stroke="#3e4a5b" stroke-width="1.2"/></svg></span>Teams</span>
      <span class="app-nav__item"><span class="app-nav__icon"><svg viewBox="0 0 10 10"><circle cx="5" cy="3.2" r="2" fill="#3e4a5b"/><path d="M1.5 9.5a3.5 3.5 0 0 1 7 0Z" fill="#3e4a5b"/></svg></span>Members</span>
      <span class="app-nav__item"><span class="app-nav__icon"><svg viewBox="0 0 10 10"><rect x="1" y="1.5" width="8" height="5.5" fill="none" stroke="#3e4a5b" stroke-width="1.2"/><path d="M3 9h4" stroke="#3e4a5b" stroke-width="1.2"/></svg></span>PTO Types</span>
      <span class="app-nav__item app-nav__item--active"><span class="app-nav__icon"><svg viewBox="0 0 10 10"><rect x="1" y="1.5" width="8" height="7.5" fill="#fff"/><rect x="1" y="1.5" width="8" height="2" fill="#cfe3f3"/></svg></span>Add PTO</span>
    </nav>
    <div class="user-chip"><span class="avatar">DM</span>Daniel Marsh<span class="user-chip__caret"></span></div>
  </header>
  <div class="content-card"></div>
  <p class="sidebar-title">EMPLOYE</p>
  <div class="search-box">Search Employees<svg viewBox="0 0 10 10"><circle cx="4.2" cy="4.2" r="3" fill="none" stroke="#0b74c1" stroke-width="1.3"/><path d="m6.5 6.5 2.5 2.5" stroke="#0b74c1" stroke-width="1.3"/></svg></div>
  <div class="employee"><span class="avatar">DM</span><div><p class="employee__name">Daniel Marsh</p><p class="employee__type">Vacation</p></div></div>
  <div class="cal-controls"><span class="ctrl-btn ctrl-btn--icon">‹</span><span class="ctrl-btn ctrl-btn--icon">›</span><span class="ctrl-btn ctrl-btn--today">Today</span></div>
  <h2 class="cal-title">August 2020</h2>
  <div class="view-switch"><span class="is-active">Month</span><span>Week</span><span>Day</span></div>
  <div class="cal">
    <div class="cal__head"><span>Sun</span><span>Mon</span><span>Tue</span><span>Wed</span><span>Thu</span><span>Fri</span><span>Sat</span></div>
    <div class="cal__body">
      <span>26</span><span>27</span><span>28</span><span>29</span><span>30</span><span>31</span><span>1</span>
      <span>2</span><span>3</span><span>4</span><span>5</span><span>6</span><span>7</span><span>8</span>
      <span>9</span><span>10</span><span>11</span><span>12</span><span>13</span><span>14</span><span>15</span>
      <span class="is-highlight">16</span><span>17</span><span>18</span><span>19</span><span>20</span><span>21</span><span>22</span>
      <span>23</span><span>24</span><span>25</span><span>26</span><span>27</span><span>28</span><span>29</span>
      <span>30</span><span>31</span><span>1</span><span>2</span><span>3</span><span>4</span><span>5</span>
      <span>6</span><span>7</span><span>8</span><span>9</span><span>10</span><span>11</span><span>12</span>
      <span>13</span><span>14</span><span>15</span><span>16</span><span>17</span><span>18</span><span>19</span>
    </div>
    <span class="cal-event cal-event--green">12a Ryan Marsh-Vacation</span>
    <span class="cal-event cal-event--blue">4a Clara Owens-Vacation</span>
    <span class="cal-event cal-event--orange">Daniel Marsh-Vacation</span>
  </div>
  <div class="scrim"></div>
  <div class="dialog">
    <h2 class="dialog__title">Add PTO</h2>
    <span class="dialog__rule"></span>
    <p class="dialog__label" style="top:30px">Member</p>
    <div class="field" style="top:36px">Daniel Marsh<span class="caret"></span></div>
    <p class="dialog__label" style="top:52px">PTO Type</p>
    <div class="field" style="top:58px">Vacation<span class="caret"></span></div>
    <p class="dialog__label" style="top:74px">Start Date</p>
    <div class="field" style="top:80px">08/11/2020<svg viewBox="0 0 10 10"><rect x="1" y="2" width="8" height="7" fill="none" stroke="#8d96a3" stroke-width=".9"/><path d="M1 4.2h8" stroke="#8d96a3" stroke-width=".9"/></svg></div>
    <p class="dialog__label" style="top:96px">End Date</p>
    <div class="field" style="top:102px">08/14/2020<svg viewBox="0 0 10 10"><rect x="1" y="2" width="8" height="7" fill="none" stroke="#8d96a3" stroke-width=".9"/><path d="M1 4.2h8" stroke="#8d96a3" stroke-width=".9"/></svg></div>
    <span class="dialog__btn dialog__btn--close">CLOSE</span>
    <span class="dialog__btn dialog__btn--save">SAVE</span>
  </div>
</section>

<!-- Teams admin -->
<section class="screen screen--teams">
  <header class="app-bar">
    <div class="brand"><span>Restday</span><span class="brand__dot"></span></div>
    <nav class="app-nav">
      <span class="app-nav__item app-nav__item--active"><span class="app-nav__icon"><svg viewBox="0 0 10 10"><path d="M5 1 9 9H1Z" fill="none" stroke="#fff" stroke-width="1.2"/></svg></span>Teams</span>
      <span class="app-nav__item"><span class="app-nav__icon"><svg viewBox="0 0 10 10"><circle cx="5" cy="3.2" r="2" fill="#3e4a5b"/><path d="M1.5 9.5a3.5 3.5 0 0 1 7 0Z" fill="#3e4a5b"/></svg></span>Members</span>
      <span class="app-nav__item"><span class="app-nav__icon"><svg viewBox="0 0 10 10"><rect x="1" y="1.5" width="8" height="5.5" fill="none" stroke="#3e4a5b" stroke-width="1.2"/><path d="M3 9h4" stroke="#3e4a5b" stroke-width="1.2"/></svg></span>PTO Types</span>
      <span class="app-nav__item"><span class="app-nav__icon"><svg viewBox="0 0 10 10"><rect x="1" y="1.5" width="8" height="7.5" fill="#3e4a5b"/></svg></span>Add PTO</span>
    </nav>
    <div class="user-chip"><span class="avatar">DM</span>Daniel Marsh<span class="user-chip__caret"></span></div>
  </header>
  <div class="search-box">Search<svg viewBox="0 0 10 10"><circle cx="4.2" cy="4.2" r="3" fill="none" stroke="#0b74c1" stroke-width="1.3"/><path d="m6.5 6.5 2.5 2.5" stroke="#0b74c1" stroke-width="1.3"/></svg></div>
  <div class="entries">Show <span class="entries__select">20 ⌄</span> Entries</div>
  <table class="data-table">
    <colgroup><col style="width:37.5px"><col style="width:48px"><col style="width:87.5px"><col style="width:50.5px"><col style="width:21px"><col></colgroup>
    <thead><tr><th>Team Name</th><th>Supervisor</th><th>Team Desc</th><th>Resource Count</th><th>Status</th><th></th></tr></thead>
    <tbody>
      <tr><td>Nursing</td><td>Clara Owens</td><td class="desc">Lorem Ipsum is simply dummy text of the printing and typesetting industry.</td><td class="count">0</td><td><span class="badge">ACTIVE</span></td><td><span class="row-actions"><svg viewBox="0 0 10 10"><rect x="1" y="2" width="7" height="7" fill="none" stroke="#0b74c1" stroke-width="1.1"/><path d="M4 6 9 1" stroke="#0b74c1" stroke-width="1.3"/></svg><svg viewBox="0 0 10 10"><rect x="2.5" y="3" width="5" height="6.5" fill="#e35b5b"/><rect x="1.5" y="1.5" width="7" height="1" fill="#e35b5b"/></svg></span></td></tr>
      <tr><td>Nursing</td><td>Clara Owens</td><td class="desc">Lorem Ipsum is simply dummy text of the printing and typesetting industry.</td><td class="count">0</td><td><span class="badge">ACTIVE</span></td><td><span class="row-actions"><svg viewBox="0 0 10 10"><rect x="1" y="2" width="7" height="7" fill="none" stroke="#0b74c1" stroke-width="1.1"/><path d="M4 6 9 1" stroke="#0b74c1" stroke-width="1.3"/></svg><svg viewBox="0 0 10 10"><rect x="2.5" y="3" width="5" height="6.5" fill="#e35b5b"/><rect x="1.5" y="1.5" width="7" height="1" fill="#e35b5b"/></svg></span></td></tr>
      <tr><td>Nursing</td><td>Clara Owens</td><td class="desc">Lorem Ipsum is simply dummy text of the printing and typesetting industry.</td><td class="count">0</td><td><span class="badge">ACTIVE</span></td><td><span class="row-actions"><svg viewBox="0 0 10 10"><rect x="1" y="2" width="7" height="7" fill="none" stroke="#0b74c1" stroke-width="1.1"/><path d="M4 6 9 1" stroke="#0b74c1" stroke-width="1.3"/></svg><svg viewBox="0 0 10 10"><rect x="2.5" y="3" width="5" height="6.5" fill="#e35b5b"/><rect x="1.5" y="1.5" width="7" height="1" fill="#e35b5b"/></svg></span></td></tr>
      <tr><td>Nursing</td><td>Clara Owens</td><td class="desc">Lorem Ipsum is simply dummy text of the printing and typesetting industry.</td><td class="count">0</td><td><span class="badge">ACTIVE</span></td><td><span class="row-actions"><svg viewBox="0 0 10 10"><rect x="1" y="2" width="7" height="7" fill="none" stroke="#0b74c1" stroke-width="1.1"/><path d="M4 6 9 1" stroke="#0b74c1" stroke-width="1.3"/></svg><svg viewBox="0 0 10 10"><rect x="2.5" y="3" width="5" height="6.5" fill="#e35b5b"/><rect x="1.5" y="1.5" width="7" height="1" fill="#e35b5b"/></svg></span></td></tr>
      <tr><td>Nursing</td><td>Clara Owens</td><td class="desc">Lorem Ipsum is simply dummy text of the printing and typesetting industry.</td><td class="count">0</td><td><span class="badge">ACTIVE</span></td><td><span class="row-actions"><svg viewBox="0 0 10 10"><rect x="1" y="2" width="7" height="7" fill="none" stroke="#0b74c1" stroke-width="1.1"/><path d="M4 6 9 1" stroke="#0b74c1" stroke-width="1.3"/></svg><svg viewBox="0 0 10 10"><rect x="2.5" y="3" width="5" height="6.5" fill="#e35b5b"/><rect x="1.5" y="1.5" width="7" height="1" fill="#e35b5b"/></svg></span></td></tr>
      <tr><td>Nursing</td><td>Clara Owens</td><td class="desc">Lorem Ipsum is simply dummy text of the printing and typesetting industry.</td><td class="count">0</td><td><span class="badge">ACTIVE</span></td><td><span class="row-actions"><svg viewBox="0 0 10 10"><rect x="1" y="2" width="7" height="7" fill="none" stroke="#0b74c1" stroke-width="1.1"/><path d="M4 6 9 1" stroke="#0b74c1" stroke-width="1.3"/></svg><svg viewBox="0 0 10 10"><rect x="2.5" y="3" width="5" height="6.5" fill="#e35b5b"/><rect x="1.5" y="1.5" width="7" height="1" fill="#e35b5b"/></svg></span></td></tr>
      <tr><td>Nursing</td><td>Clara Owens</td><td class="desc">Lorem Ipsum is simply dummy text of the printing and typesetting industry.</td><td class="count">0</td><td><span class="badge">ACTIVE</span></td><td><span class="row-actions"><svg viewBox="0 0 10 10"><rect x="1" y="2" width="7" height="7" fill="none" stroke="#0b74c1" stroke-width="1.1"/><path d="M4 6 9 1" stroke="#0b74c1" stroke-width="1.3"/></svg><svg viewBox="0 0 10 10"><rect x="2.5" y="3" width="5" height="6.5" fill="#e35b5b"/><rect x="1.5" y="1.5" width="7" height="1" fill="#e35b5b"/></svg></span></td></tr>
      <tr><td>Nursing</td><td>Clara Owens</td><td class="desc">Lorem Ipsum is simply dummy text of the printing and typesetting industry.</td><td class="count">0</td><td><span class="badge">ACTIVE</span></td><td><span class="row-actions"><svg viewBox="0 0 10 10"><rect x="1" y="2" width="7" height="7" fill="none" stroke="#0b74c1" stroke-width="1.1"/><path d="M4 6 9 1" stroke="#0b74c1" stroke-width="1.3"/></svg><svg viewBox="0 0 10 10"><rect x="2.5" y="3" width="5" height="6.5" fill="#e35b5b"/><rect x="1.5" y="1.5" width="7" height="1" fill="#e35b5b"/></svg></span></td></tr>
    </tbody>
  </table>
  <p class="table-info">Showing 1 to 12 of 15 entries</p>
  <nav class="pager">
    <span class="pager__edge">‹ Prev</span>
    <span class="pager__page">1</span><span class="pager__page pager__page--active">2</span><span class="pager__page">3</span><span>...</span><span class="pager__page">82</span>
    <span class="pager__edge pager__edge--next">Next ›</span>
  </nav>
</section>

<!-- Profile -->
<section class="screen screen--profile">
  <header class="app-bar">
    <div class="brand"><span>Restday</span><span class="brand__dot"></span></div>
    <nav class="app-nav">
      <span class="app-nav__item"><span class="app-nav__icon"><svg viewBox="0 0 10 10"><path d="M5 1 9 9H1Z" fill="none" stroke="#3e4a5b" stroke-width="1.2"/></svg></span>Teams</span>
      <span class="app-nav__item"><span class="app-nav__icon"><svg viewBox="0 0 10 10"><circle cx="5" cy="3.2" r="2" fill="#3e4a5b"/><path d="M1.5 9.5a3.5 3.5 0 0 1 7 0Z" fill="#3e4a5b"/></svg></span>Members</span>
      <span class="app-nav__item"><span class="app-nav__icon"><svg viewBox="0 0 10 10"><rect x="1" y="1.5" width="8" height="5.5" fill="none" stroke="#3e4a5b" stroke-width="1.2"/><path d="M3 9h4" stroke="#3e4a5b" stroke-width="1.2"/></svg></span>PTO Types</span>
      <span class="app-nav__item"><span class="app-nav__icon"><svg viewBox="0 0 10 10"><rect x="1" y="1.5" width="8" height="7.5" fill="#3e4a5b"/></svg></span>Add PTO</span>
    </nav>
    <div class="user-chip"><span class="avatar">DM</span>Daniel Marsh<span class="user-chip__caret"></span></div>
  </header>
  <div class="profile-card">
    <span class="avatar">DM</span>
    <p class="profile-name">Daniel Marsh</p>
    <p class="profile-email">info@danielmarsh.example</p>
    <div class="account">
      <h2 class="account__title">Account</h2>
      <p class="account__label" style="top:38px">User name</p>
      <div class="field" style="top:43px">Daniel</div>
      <p class="account__label" style="top:60px">Email</p>
      <div class="field" style="top:65.5px">info@danielmarsh.example</div>
      <p class="account__label" style="top:83px">Password</p>
      <div class="field" style="top:88px">••••••••••••••</div>
      <p class="account__label" style="top:105px">Full Name</p>
      <div class="field" style="top:110px">Daniel Marsh</div>
      <p class="account__label" style="top:128px">Title</p>
      <div class="field" style="top:133px">Administrator</div>
      <p class="account__label" style="top:150px">Language</p>
      <div class="field field--select" style="top:155px"><span><i class="flag"></i>English</span><span class="caret"></span></div>
      <span class="account__save">SAVE</span>
    </div>
  </div>
</section>

</body>
</html>
```